VERIDAX Need a luxury modern business card designed.

Need a luxury modern business card designed. refer to the uploaded files for the company name and logo in the zip file under source files. i will making my descion on monday. so please send in before then so if we need to edit we will have the time. we have a trade show coming up and im on a deadline for printer.

Target Market(s)

high end clients

Contact Information for Business Card

Company nAme and logo. Calvin Ostrow Co-Founder / Project Manager Office # 416-555-0193 Cell # 416-555-0147 VERIDAX.CA Calvin@veridax.ca

Font styles to use
Other font styles liked:
• Modern

Requirements
Must have
• Company name and logo, contact info, using the black, gold and white color scheme.

```html
<!DOCTYPE html>
<html lang="en">
<head>
<meta charset="utf-8">
<title>VERIDAX Business Card</title>
<link href="https://fonts.googleapis.com/css2?family=Oswald:wght@400;500&family=Poppins:wght@300;400&display=swap" rel="stylesheet">
<style>
  :root {
    --backdrop: #1b1b1b;
    --charcoal: #2e2e2e;
    --gold: #a89a63;
    --gold-light: #bfb07a;
    --gold-deep: #978955;
    --white: #ffffff;
    --rule: #8a8a8a;
  }
  * { margin: 0; padding: 0; box-sizing: border-box; }
  html, body {
    width: 1200px; height: 1108px; overflow: hidden;
    background: var(--backdrop);
  }
  .canvas {
    position: relative; width: 1200px; height: 1108px;
    display: flex; justify-content: center; align-items: center; gap: 60px;
  }
  .card {
    width: 440px; height: 770px; position: relative;
    box-shadow: 0 12px 30px rgba(0,0,0,0.45);
  }
  .card--front {
    background: var(--charcoal);
    border-bottom: 4px solid var(--gold);
    display: flex; flex-direction: column; align-items: center;
    padding-top: 190px; color: var(--white); text-align: center;
  }
  .brand {
    display: flex; flex-direction: column; align-items: center;
  }
  .brand__name {
    font-family: "Poppins", sans-serif; font-weight: 300;
    font-size: 34px; letter-spacing: 9px; color: var(--white);
    padding-left: 9px;
  }
  .brand__tagline {
    margin-top: 6px; padding: 3px 0 4px 0;
    border-top: 1px solid var(--rule); border-bottom: 1px solid var(--rule);
    width: 230px;
    font-family: "Poppins", sans-serif; font-size: 8px; letter-spacing: 3px;
    color: var(--white);
  }
  .person { margin-top: 34px; }
  .person__name {
    font-family: "Oswald", sans-serif; font-weight: 500;
    font-size: 27px; color: var(--gold); text-transform: uppercase;
    letter-spacing: 0.5px; line-height: 1.1;
  }
  .person__title {
    font-family: "Oswald", sans-serif; font-weight: 500;
    font-size: 17px; color: var(--white); text-transform: uppercase;
    line-height: 1.2;
  }
  .contact {
    margin-top: 22px; list-style: none;
    font-family: "Poppins", sans-serif; font-weight: 400;
    font-size: 16px; line-height: 1.3; color: var(--white);
  }
  .divider {
    margin-top: 14px; width: 220px; height: 1px; background: var(--rule);
  }
  .website {
    margin-top: 14px;
    font-family: "Poppins", sans-serif; font-size: 15px;
    letter-spacing: 4px; color: var(--white);
  }
  .card--back {
    background: linear-gradient(150deg, var(--gold-light), var(--gold) 50%, var(--gold-deep));
  }
  .back-mark {
    position: absolute; right: 70px; bottom: 130px;
    font-family: "Poppins", sans-serif; font-weight: 300;
    font-size: 22px; letter-spacing: 5px; color: var(--white);
  }
</style>
</head>
<body>
  <main class="canvas">
    <section class="card card--front">
      <div class="brand">
        <div class="brand__name">VERIDAX</div>
        <div class="brand__tagline">LUXURY LANDSCAPES</div>
      </div>
      <div class="person">
        <div class="person__name">Calvin Ostrow</div>
        <div class="person__title">Co-Founder / Project Manager</div>
      </div>
      <ul class="contact">
        <li>P. 416-555-0193</li>
        <li>C. 416-555-0147</li>
        <li>Calvin@veridax.ca</li>
      </ul>
      <div class="divider"></div>
      <div class="website">www.veridax.ca</div>
    </section>
    <section class="card card--back" role="img" aria-label="Gold card back with embossed repeating brand pattern">
      <div class="back-mark">VERIDAX</div>
    </section>
  </main>
</body>
</html>
```